Marlowick APP redesign and color change

I am looking for a new design for my app. Please see the attached current design.

Currently, I have a functioning app but the colors and design are awful!
The logo is great but the rest of the app needs a refresh.
(Logo hi res not yet available but will upload soon.)
New colors or anything that is cutting edge.

Basically: It is a secure social media app within a school system where the teachers, students and parents can text, exchange photos, plan curriculum, etc.

I NEED ONLY landing page with a new look!
Looking for one distinct design for the landing page with new look.
The developer will apply this one design towards the rest of the pages/app screens.

Because part of the social media I need the feel and look of what is now the trend. Something that will attract and keep the client(s) interested. I am really leaving all the creative work to the designer and open to any suggestions.
Updates

Target Market(s)

Schools, community, teachers, students, colleges, sport teams

Industry/Entity Type

Non Profit

Font styles to use
Serif
Sans Serif

Colors

Designer to choose colors to be used in the design.

Requirements
Must have
• Sharp, trendy, millennial feel
Nice to have
• Up to designer
Should not have
• Up to designer

```html
<!DOCTYPE html>
<html lang="en">
<head>
<meta charset="utf-8">
<title>Marlowick — Log In</title>
<link rel="stylesheet" href="https://fonts.googleapis.com/css2?family=Noto+Sans:wght@400;700&display=swap">
<style>
  :root {
    --teal-core: #19b2d4;
    --teal-mid: #0d88a8;
    --teal-deep: #064c6a;
    --teal-haze: rgba(120, 200, 220, 0.22);
    --white: #ffffff;
    --button-fill: rgba(255, 255, 255, 0.45);
  }
  html, body {
    margin: 0;
    padding: 0;
    overflow: hidden;
  }
  .screen {
    position: relative;
    width: 675px;
    height: 1200px;
    overflow: hidden;
    background: radial-gradient(ellipse 70% 60% at 50% 52%, var(--teal-core) 0%, var(--teal-mid) 50%, var(--teal-deep) 100%);
    font-family: "Noto Sans", sans-serif;
    color: var(--white);
  }
  .backdrop-pattern {
    position: absolute;
    inset: 0;
    background:
      radial-gradient(ellipse 62% 46% at 50% 50%, transparent 0%, transparent 55%, var(--teal-haze) 72%, transparent 90%),
      radial-gradient(ellipse 55% 22% at 50% 84%, var(--teal-haze) 0%, transparent 100%),
      radial-gradient(ellipse 75% 28% at 50% 12%, var(--teal-haze) 0%, transparent 100%);
  }
  .brand-mark {
    position: absolute;
    left: 207px;
    top: 400px;
    width: 260px;
    height: 260px;
  }
  .brand-name {
    position: absolute;
    left: 0;
    right: 0;
    top: 684px;
    margin: 0;
    text-align: center;
    font-size: 32px;
    font-weight: 700;
    letter-spacing: 0.42em;
    padding-left: 0.42em;
    line-height: 42px;
  }
  .tagline {
    position: absolute;
    left: 0;
    right: 0;
    top: 727px;
    margin: 0;
    text-align: center;
    font-size: 15.5px;
    font-weight: 400;
    line-height: 20px;
  }
  .login-button {
    position: absolute;
    left: 188px;
    top: 772px;
    width: 298px;
    height: 49px;
    border: none;
    border-radius: 25px;
    background: var(--button-fill);
    color: var(--white);
    font-family: "Noto Sans", sans-serif;
    font-size: 40px;
    line-height: 49px;
    padding: 0;
    text-align: center;
  }
</style>
</head>
<body>
  <main class="screen">
    <div class="backdrop-pattern" role="img" aria-label="Large faint brand pattern spreading across the background"></div>
    <svg class="brand-mark" viewBox="0 0 260 260" aria-hidden="true">
      <circle cx="130" cy="130" r="124" fill="none" stroke="#ffffff" stroke-width="6"/>
    </svg>
    <h1 class="brand-name">MARLOWICK</h1>
    <p class="tagline">SECURITY THROUGH TRANSPARENCY</p>
    <button class="login-button" type="button">Log In</button>
  </main>
</body>
</html>
```